A Label for an ECO Friendly Spirit Company

Design a label which can be used for vodka and gin (London Dry Gin). It should be Square type Like the Shape File you see in the uploads. VORK means Local Eco friendly Authentic and Fair. We want a cool and slim label that calls for eco-friendly. We want to use it for our premium
Vodka and our London Dry Gin. Please use the logo and design it in Square Type.

40%vol, 700ml

Target Market(s)

spirits and events

Industry/Entity Type

SPIRITS

Colors
00AB8E
00BBA5
67D7C9
C6EFE9
E9F9F6
59FF00
82FF00
B8FF75
E3FFCB
F4FFEA

Requirements
Must have
• Logo from VORK, Squaee Shape

```html
<!DOCTYPE html>
<html lang="en">
<head>
<meta charset="utf-8">
<title>VORK Vodka &amp; Gin Label</title>
<link rel="stylesheet" href="https://fonts.googleapis.com/css2?family=Fascinate&family=Poiret+One&family=Montserrat:wght@600&family=Cormorant+Garamond:wght@400&display=swap">
<style>
  :root {
    --stage: #c9d6e4;
    --label: #f4f8fa;
    --ink: #111111;
    --ink-soft: #3a3a3a;
    --teal-deep: #00ab8e;
    --teal: #3fd0b5;
    --teal-light: #c6efe9;
    --lime: #82ff00;
    --brand: #00bba5;
  }
  * { margin: 0; padding: 0; box-sizing: border-box; }
  html, body {
    width: 1200px;
    height: 1200px;
    overflow: hidden;
    background: var(--stage);
  }
  .canvas {
    position: relative;
    width: 1200px;
    height: 1200px;
    display: flex;
    justify-content: center;
  }
  .label {
    position: relative;
    width: 580px;
    height: 1200px;
    background: var(--label);
    overflow: hidden;
  }
  .brand {
    position: absolute;
    top: 62px;
    left: 60px;
    display: flex;
    align-items: center;
    gap: 34px;
  }
  .brand-square {
    width: 120px;
    height: 120px;
    background: var(--lime);
    border-radius: 10px;
  }
  .brand-name {
    font-family: "Montserrat", sans-serif;
    font-weight: 600;
    font-size: 104px;
    line-height: 1;
    letter-spacing: 2px;
    color: var(--brand);
  }
  .product-title {
    position: absolute;
    top: 300px;
    left: 0;
    width: 100%;
    text-align: center;
    font-family: "Fascinate", serif;
    font-size: 138px;
    line-height: 178px;
    color: var(--ink);
  }
  .product-style {
    position: absolute;
    top: 662px;
    left: 0;
    width: 100%;
    text-align: center;
    font-family: "Poiret One", sans-serif;
    font-size: 42px;
    color: var(--ink-soft);
    letter-spacing: 1px;
  }
  .base-band {
    position: absolute;
    left: 0;
    top: 0;
    width: 580px;
    height: 1200px;
  }
  .volume {
    position: absolute;
    top: 975px;
    left: 96px;
    font-family: "Cormorant Garamond", serif;
    font-size: 32px;
    color: var(--ink-soft);
    word-spacing: 22px;
  }
</style>
</head>
<body>
  <main class="canvas">
    <section class="label">
      <svg class="base-band" viewBox="0 0 580 1200" aria-hidden="true">
        <path d="M0 936 Q130 840 252 787 Q400 860 580 972 L580 1200 L0 1200 Z" fill="var(--teal)"/>
        <path d="M252 787 Q360 870 420 960 Q470 1040 580 1070 L580 972 Q400 860 252 787 Z" fill="var(--teal-light)" opacity="0.55"/>
        <path d="M0 960 Q130 870 252 820 Q390 890 440 990" fill="none" stroke="var(--label)" stroke-width="10" opacity="0.8"/>
      </svg>
      <div class="brand">
        <div class="brand-square"></div>
        <div class="brand-name">VORK</div>
      </div>
      <h1 class="product-title">Vodka<br>&amp; Gin</h1>
      <p class="product-style">London Dry Gin</p>
      <p class="volume">40%vol 700ml</p>
    </section>
  </main>
</body>
</html>
```